Environmental Group Website Template

We want a website template for an environmental cause. The website should have a dark content area that is transparent. The website text and icons are white.
The background is a nature scene. The background image repeats.
Industry/Entity Type
Group

```html
<!DOCTYPE html>
<html lang="en">
<head>
<meta charset="utf-8">
<title>Tidewater Circle</title>
<link href="https://fonts.googleapis.com/css2?family=Arimo:wght@400;700&display=swap" rel="stylesheet">
<style>
:root{
  --orange:#f2622e;
  --orange-light:#ff7a45;
  --green:#4f9a35;
  --green-bright:#5cb544;
  --white:#ffffff;
  --soft-white:rgba(255,255,255,0.88);
  --panel-head:rgba(22,28,34,0.72);
  --panel-body:rgba(22,28,34,0.66);
  --card:rgba(10,14,18,0.55);
  --card-edge:rgba(255,255,255,0.28);
  --footer-top:#3b3b3b;
  --footer-bottom:#1b1b1b;
}
*{box-sizing:border-box;margin:0;padding:0}
html,body{width:1185px;height:1200px;overflow:hidden}
body{font-family:"Arimo",Arial,sans-serif;color:var(--white);position:relative}
.scenery{position:absolute;inset:0;
  background:linear-gradient(180deg,#b9c9dc 0%,#d7dde4 16%,#e9dcc0 24%,#8ea0ad 27%,#7b8c5a 33%,#5e6f7f 45%,#4b5d75 60%,#6b7f54 78%,#4a5b6e 100%);}
.site{position:absolute;left:169px;top:57px;width:846px;height:1143px}
.masthead{height:130px;background:var(--panel-head);position:relative}
.brand{position:absolute;left:22px;top:44px;display:flex;align-items:center;gap:12px}
.brand-dot{width:34px;height:34px;border-radius:50%;background:var(--orange)}
.brand-name{font-size:22px;font-weight:400;color:var(--white)}
.search{position:absolute;left:620px;top:58px;width:181px;height:34px;border:1px solid rgba(255,255,255,0.5);background:rgba(255,255,255,0.12);display:flex;align-items:center;padding:0 8px;font-size:12px;color:var(--soft-white);justify-content:space-between}
.main-nav{height:46px;background:linear-gradient(180deg,var(--orange-light),var(--orange));display:flex;align-items:center;padding-left:14px}
.main-nav a{color:#fff;font-weight:700;font-size:12px;text-decoration:none;height:46px;line-height:46px;padding:0 14px;margin-right:19px;position:relative}
.main-nav a.current::after{content:"";position:absolute;left:0;right:0;bottom:0;height:3px;background:var(--green-bright)}
.hero{height:446px;position:relative;background:linear-gradient(160deg,#c8d8e8 0%,#9fb3c4 30%,#6f8a5a 60%,#4e6a3a 100%)}
.hero-dots{position:absolute;left:20px;bottom:16px;display:flex;gap:11px;align-items:center}
.hero-dots span{width:12px;height:12px;border-radius:50%;background:#fff}
.hero-dots span.active{background:var(--orange);box-shadow:0 0 0 2px #fff}
.about{height:440px;background:var(--panel-body);position:relative}
.about-title{position:absolute;top:26px;left:0;right:0;text-align:center;font-size:26px;font-weight:700;color:var(--white);letter-spacing:.3px}
.about-title em{font-style:normal;color:var(--orange)}
.about-text{position:absolute;top:71px;left:50px;right:46px;text-align:center;font-size:12px;line-height:20px;color:var(--soft-white)}
.feature{position:absolute;top:201px;width:248px;height:188px;background:var(--card);border:1px solid var(--card-edge);box-shadow:0 1px 3px rgba(0,0,0,.3);text-align:center}
.feature-icon{position:absolute;left:79px;top:-44px;width:90px;height:90px;border-radius:50%;background:var(--green);display:flex;align-items:center;justify-content:center}
.feature h3{margin-top:56px;font-size:16px;font-weight:700;color:var(--orange);letter-spacing:.3px}
.feature p{margin:8px 20px 0;font-size:11px;line-height:17.5px;color:var(--soft-white)}
.feature a{display:inline-block;margin-top:8px;font-size:13px;font-weight:700;color:var(--orange);text-decoration:none}
.site-footer{position:absolute;left:0;top:1062px;width:846px;height:81px;background:linear-gradient(180deg,var(--footer-top),var(--footer-bottom));display:flex;align-items:center;justify-content:space-between;padding:0 16px 0 20px}
.social{display:flex;gap:11px}
.social span{width:26px;height:26px;border-radius:4px;background:#6d747c}
.copyright{color:#fff;font-size:11px}
</style>
</head>
<body>
<div class="scenery" role="img" aria-label="Coastal marsh with grass and open water under a pale sky"></div>
<div class="site">
  <header class="masthead">
    <div class="brand"><span class="brand-dot"></span><span class="brand-name">Tidewater Circle</span></div>
    <div class="search">Search...
      <svg width="20" height="20" viewBox="0 0 20 20"><circle cx="8" cy="8" r="6" fill="none" stroke="#fff" stroke-width="2.6"/><line x1="12.5" y1="12.5" x2="18" y2="18" stroke="#fff" stroke-width="3" stroke-linecap="round"/></svg>
    </div>
  </header>
  <nav class="main-nav">
    <a class="current" href="#">Home</a><a href="#">About</a><a href="#">Explore</a><a href="#">Challenses</a><a href="#">Solutions</a><a href="#">Events</a><a href="#">News</a>
  </nav>
  <section class="hero" role="img" aria-label="Three generations of a family smiling by a lake, holding a fish and fishing rods">
    <div class="hero-dots"><span></span><span class="active"></span><span></span><span></span></div>
  </section>
  <section class="about">
    <h2 class="about-title">About <em>Tidewater Circle</em></h2>
    <p class="about-text">Lorem ipsum dolor sit amet, consectetur adipiscing elit, sed do eiusmod tempor incididunt ut labore et dolore magna aliqua. Ut enim ad minim velit esse cillum dolore eu fugiat nulla pariatur. Excepteur sint occaecat cupidatat non proident, sunt in culpa qui officia deserunt mollit anim id est laborum Sed ut perspiciatis unde omnis iste natus error sit voluptatem doloremque.</p>

    <article class="feature" style="left:15px">
      <div class="feature-icon">
        <svg width="52" height="46" viewBox="0 0 52 46" fill="none" stroke="#fff" stroke-width="3" stroke-linejoin="round"><circle cx="26" cy="9" r="5"/><circle cx="12" cy="14" r="4"/><circle cx="40" cy="14" r="4"/><path d="M18 44V22l8 8 8-8v22"/><path d="M5 40V24h10M47 40V24H37"/></svg>
      </div>
      <h3>Volunteers</h3>
      <p>Lorem ipsum dolor sit amet, consectetur adipiscing elit, sed do eiusmod tempor incididunt ut labore et dolore magna aliqua Ut enim</p>
      <a href="#">Read More »</a>
    </article>

    <article class="feature" style="left:299px">
      <div class="feature-icon">
        <svg width="54" height="50" viewBox="0 0 54 50" fill="none" stroke="#fff" stroke-width="3.5"><circle cx="30" cy="16" r="8"/><path d="M30 2v5M30 25v5M16 16h5M39 16h5M20 6l3.5 3.5M36.5 22.5L40 26M40 6l-3.5 3.5M23.5 22.5L20 26" stroke-linecap="round"/><path d="M4 38h12l10 3h14l10-5M4 46h10l12 2 22-10" stroke-linecap="round" stroke-linejoin="round"/></svg>
      </div>
      <h3>Spport Our Work</h3>
      <p>Lorem ipsum dolor sit amet, consectetur adipiscing elit, sed do eiusmod tempor incididunt ut labore et dolore magna aliqua Ut enim</p>
      <a href="#">Read More »</a>
    </article>

    <article class="feature" style="left:583px">
      <div class="feature-icon">
        <svg width="52" height="48" viewBox="0 0 52 48" fill="none" stroke="#fff" stroke-width="3" stroke-linejoin="round"><path d="M6 16h10l22-12v36L16 28H6z"/><path d="M12 28l6 16h7l-5-16"/><path d="M42 16a6 6 0 0 1 0 12"/></svg>
      </div>
      <h3>Make your voice heard</h3>
      <p>Lorem ipsum dolor sit amet, consectetur adipiscing elit, sed do eiusmod tempor incididunt ut labore et dolore magna aliqua Ut enim</p>
      <a href="#">Read More »</a>
    </article>
  </section>
  <footer class="site-footer">
    <div class="social" aria-label="Social links"><span></span><span></span><span></span><span></span><span></span><span></span></div>
    <p class="copyright">Copyright © 2014. All Rights Reserved.</p>
  </footer>
</div>
</body>
</html>
```